Brindlewood Property Management, L.L.C
Brindlewood Property Management, L.L.C - Financial Services
Creative Brief
Professional
Doreen Whitlock,CAM
President
P.O. Box 572816 Naples, FL. 34117
info@brindlewoodprop.com
www.brindlewoodprop.com
I am open to clear business cards or two sides if a two sided design is used see comment below.
Logo on back of card if this option is designed

```html
<!DOCTYPE html>
<html lang="en">
<head>
<meta charset="utf-8">
<title>Brindlewood Property Management – Business Cards</title>
<link rel="stylesheet" href="https://fonts.googleapis.com/css2?family=Arimo:wght@400;700&display=swap">
<style>
  :root {
    --page-bg: #ffffff;
    --front-card: #000000;
    --front-edge: #8e8e8e;
    --back-card: #9c9c9c;
    --back-outline: #2a2a2a;
    --back-shadow: #3a3a3a;
    --brand-blue: #2f5bd0;
    --brand-mark: #2a58c9;
    --mark-ring: #101010;
    --text-light: #ffffff;
    --text-dark: #1a1a1a;
    --icon-front: #3b5fc7;
    --icon-back: #2a3f86;
  }
  * { margin: 0; padding: 0; box-sizing: border-box; }
  html, body { width: 1200px; height: 956px; overflow: hidden; background: var(--page-bg); }
  body { position: relative; font-family: "Arimo", Arial, sans-serif; }

  .card { position: absolute; top: 13px; width: 528px; height: 930px; border-radius: 34px; overflow: hidden; }

  .card--front { left: 12px; background: var(--front-edge); }
  .card--front .card-face {
    position: absolute; left: 22px; right: 22px; top: 0; bottom: 0;
    background: var(--front-card);
  }

  .card--back {
    left: 658px; width: 530px; background: var(--back-card);
    border: 3px solid var(--back-outline);
    box-shadow: 6px 6px 0 var(--back-shadow);
    overflow: visible;
  }

  .brand-mark {
    position: absolute; left: 50%; top: 20px; width: 156px; height: 156px;
    margin-left: -78px; border-radius: 50%;
    background: var(--brand-mark);
  }
  .card--back .brand-mark { top: 18px; border: 8px solid var(--mark-ring); background: #6f7fa8; }

  .brand-name {
    position: absolute; left: 0; right: 0; text-align: center;
    color: var(--brand-blue); font-weight: 400; line-height: 1;
  }
  .brand-name .primary { display: block; font-size: 44px; letter-spacing: 2px; }
  .brand-name .secondary { display: block; font-size: 24px; letter-spacing: 1px; margin-top: 6px; }
  .card--front .brand-name { top: 208px; }
  .card--back .brand-name { top: 206px; }

  .holder { position: absolute; left: 80px; top: 362px; color: var(--text-light); }
  .holder-name { font-size: 33px; font-weight: 700; }
  .holder-title { font-size: 31px; margin-top: 6px; }

  .contacts { position: absolute; list-style: none; font-size: 22px; line-height: 31px; }
  .card--front .contacts { left: 28px; top: 798px; color: var(--text-light); }
  .card--back .contacts { left: 50px; top: 796px; color: var(--text-dark); }
  .contacts li { display: flex; align-items: center; }
  .contacts svg { width: 22px; height: 22px; margin-right: 18px; flex: none; }
  .card--front .contacts svg { fill: var(--icon-front); }
  .card--back .contacts svg { fill: var(--icon-back); }
</style>
</head>
<body>

<section class="card card--front">
  <div class="card-face">
    <div class="brand-mark"></div>
    <div class="brand-name">
      <span class="primary">BRINDLEWOOD</span>
      <span class="secondary">PROPERTY MANAGEMENT</span>
    </div>
    <div class="holder">
      <p class="holder-name">Doreen Whitlock,CAM</p>
      <p class="holder-title">President</p>
    </div>
    <ul class="contacts">
      <li><svg viewBox="0 0 24 24"><path d="M7 2c1 0 2 3 2.5 5 .2 1-1.5 2-1.5 3 1 3 3 5 5 6 1 0 2-1.7 3-1.5 2 .5 5 1.5 5 2.5 0 2-2 5-4 5C9 22 2 15 2 7c0-2 3-5 5-5z"/></svg>239.555.0147</li>
      <li><svg viewBox="0 0 24 24"><circle cx="12" cy="12" r="10"/></svg>www.brindlewoodprop.com</li>
      <li><svg viewBox="0 0 24 24"><path d="M2 5h20v14H2z"/></svg>info@brindlewoodprop.com</li>
      <li><svg viewBox="0 0 24 24"><path d="M12 2l10 9h-3v11h-5v-7h-4v7H5V11H2z"/></svg>P.O.Box 572816 Naples, FL. 34117</li>
    </ul>
  </div>
</section>

<section class="card card--back">
  <div class="brand-mark"></div>
  <div class="brand-name">
    <span class="primary">BRINDLEWOOD</span>
    <span class="secondary">PROPERTY MANAGEMENT</span>
  </div>
  <ul class="contacts">
    <li><svg viewBox="0 0 24 24"><path d="M7 2c1 0 2 3 2.5 5 .2 1-1.5 2-1.5 3 1 3 3 5 5 6 1 0 2-1.7 3-1.5 2 .5 5 1.5 5 2.5 0 2-2 5-4 5C9 22 2 15 2 7c0-2 3-5 5-5z"/></svg>239.555.0147</li>
    <li><svg viewBox="0 0 24 24"><circle cx="12" cy="12" r="10"/></svg>www.brindlewoodprop.com</li>
    <li><svg viewBox="0 0 24 24"><path d="M2 5h20v14H2z"/></svg>info@brindlewoodprop.com</li>
    <li><svg viewBox="0 0 24 24"><path d="M12 2l10 9h-3v11h-5v-7h-4v7H5V11H2z"/></svg>P.O.Box 572816 Naples, FL. 34117</li>
  </ul>
</section>

</body>
</html>
```